Home Remodeler Needs a Website!

Single page (plus contact form) website for small home remodeling company. He's got a few pictures he'd like on the site and needs some basic text. He likes clean, simple designs and is "more traditional" in his stylistic preferences. Most of his business comes from word-of-mouth advertising and so the site is just something he needs for people to feel more comfortable with his business.
Updates

Target Market(s)

People who want to remodel their homes

Coding

Coded - Design and coding required

Number of Pages Required

2 page

Requirements
Must have
• Main page to include some or all of the attached images, contact page. Neutral colors. Old domain: brindlecoveroofing.com New domain: mq-outfitters.com You can pull text from the old site or update it.
Should not have
• No loud colors/loud visual elements

```html
<!DOCTYPE html>
<html lang="en">
<head>
<meta charset="utf-8">
<title>MQ Outfitters — Home Construction &amp; Remodeling</title>
<link href="https://fonts.googleapis.com/css2?family=Poppins:wght@300;400;500;600;700&display=swap" rel="stylesheet">
<style>
:root{
  --olive:#6b7b1e;
  --olive-dark:#5a6819;
  --ink:#1d1d1d;
  --muted:#333;
  --light-bg:#efefef;
  --footer:#3c4638;
  --white:#fff;
}
*{box-sizing:border-box;margin:0;padding:0}
html,body{width:1200px;height:3058px;overflow:hidden}
body{font-family:'Poppins',sans-serif;color:var(--ink);background:var(--white);position:relative}

/* header */
.site-header{position:absolute;left:0;top:0;width:1200px;height:77px;background:var(--white)}
.brand{position:absolute;left:115px;top:27px;width:124px;text-align:center;color:var(--olive);font-weight:600;font-size:14px;letter-spacing:.5px;white-space:nowrap}
.main-nav{position:absolute;left:0;top:0;width:1200px;height:77px;font-size:12.5px}
.main-nav a{position:absolute;top:25px;height:29px;line-height:29px;color:var(--ink);text-decoration:none;white-space:nowrap}
.main-nav a.active{border:2px solid var(--olive);color:var(--olive);width:74px;text-align:center;line-height:25px}
.socials{display:flex;gap:9px}
.socials span{width:22px;height:22px;border:1px solid #999;border-radius:50%;display:block}
.socials span.on{border-color:var(--olive)}
.header-socials{position:absolute;left:830px;top:28px}
.quote-btn{position:absolute;left:966px;top:23px;width:106px;height:31px;background:var(--olive);color:var(--white);font-size:12px;font-weight:600;text-align:center;line-height:31px}

/* hero */
.hero{position:absolute;left:0;top:77px;width:1200px;height:488px;background:linear-gradient(180deg,#2b3140 0%,#4a4b4c 45%,#2a2826 100%)}
.hero-title{position:absolute;top:182px;width:1200px;text-align:center;color:var(--white);font-size:29px;font-weight:600}
.hero-sub{position:absolute;top:223px;width:1200px;text-align:center;color:var(--white);font-size:17.5px;font-weight:300}
.hero-btn{position:absolute;left:537px;top:267px;width:126px;height:35px;border:2px solid var(--white);background:var(--olive);color:var(--white);font-size:13px;font-weight:500;text-align:center;line-height:31px}
.dots{position:absolute;top:459px;left:578px;display:flex;gap:8px}
.dots span{width:10px;height:10px;border:1.5px solid var(--white);border-radius:50%}
.dots span.on{background:var(--olive);border-color:var(--olive)}

/* section headings */
.section-head{position:absolute;width:1200px;text-align:center}
.section-head .ornament{display:block;margin:0 auto 4px;width:24px;height:12px;background:var(--olive)}
.section-head h2{font-size:24px;font-weight:700;color:var(--olive);letter-spacing:.3px;line-height:30px}

/* about */
.about-lead{position:absolute;top:704px;width:1200px;text-align:center;font-size:15.5px;font-weight:500}
.about-text{position:absolute;top:734px;width:1200px;text-align:center;font-size:11.5px;line-height:19px;color:var(--muted)}
.outline-btn{position:absolute;left:528px;top:824px;width:155px;height:34px;border:1px solid var(--olive);color:var(--olive);font-size:11.5px;font-weight:500;text-align:center;line-height:32px}

/* products */
.products{position:absolute;left:0;top:922px;width:1200px;height:1021px;background:var(--light-bg)}
.card-photo{position:absolute;width:381px;height:297px}
.card-cap{position:absolute;width:326px;height:65px;background:var(--white);display:flex;align-items:center;justify-content:center;gap:18px;color:var(--olive)}
.card-cap .num{font-size:34px;font-weight:400}
.card-cap .label{font-size:14.5px;font-weight:400;line-height:16px}
.solid-btn{position:absolute;left:553px;top:1839px;width:125px;height:33px;background:var(--olive);color:var(--white);font-size:11.5px;text-align:center;line-height:33px}

/* resources */
.resources{position:absolute;left:0;top:1943px;width:1200px;height:380px;background:linear-gradient(100deg,#2a2f25,#3c4032 55%,#2a2e24)}
.res-intro{position:absolute;top:2050px;width:1200px;text-align:center;color:var(--white);font-size:15px;font-weight:300}
.res-card{position:absolute;top:2108px;width:242px;height:101px;background:var(--white);display:flex;align-items:center;justify-content:center;text-align:center}
.res-name{font-size:15px;font-weight:600;letter-spacing:1.5px;white-space:nowrap}
.res-cap{position:absolute;top:2222px;width:242px;text-align:center;color:var(--white);font-size:12px;line-height:16px}

/* consultation */
.map{position:absolute;left:147px;top:2393px;width:455px;height:391px;background:linear-gradient(135deg,#eef0ee,#e2e6e4 60%,#cfe3d2)}
.consult{position:absolute;left:602px;top:2393px;width:450px;height:363px;background:var(--olive)}
.consult h3{position:absolute;left:76px;top:40px;color:var(--white);font-size:18px;font-weight:600}
.field{position:absolute;left:77px;width:297px;height:28px;background:var(--white);border:1px solid #ccc;font-size:10px;color:#999;padding:7px 10px}
.submit{position:absolute;left:77px;top:309px;width:85px;height:30px;border:1.5px solid var(--white);color:var(--white);font-size:11px;text-align:center;line-height:27px}

/* footer */
.site-footer{position:absolute;left:0;top:2756px;width:1200px;height:259px;background:var(--footer);color:var(--white)}
.foot-nav{position:absolute;left:395px;top:50px;display:flex;gap:34px;font-size:11px}
.foot-nav .active{color:#8a9a33;text-decoration:underline}
.foot-rule{position:absolute;left:127px;top:87px;width:946px;height:1px;background:#56604f}
.contact{position:absolute;left:127px;top:118px;font-size:12.5px;line-height:21px}
.contact .call{font-size:17.5px;font-weight:300;line-height:26px}
.contact b{font-weight:600}
.address{position:absolute;left:127px;top:200px;font-size:11.5px;line-height:16px}
.address b{font-weight:600}
.foot-brand{position:absolute;left:500px;top:187px;width:200px;text-align:center;color:#5f6e26;font-weight:600;font-size:15px;white-space:nowrap}
.hours{position:absolute;left:834px;top:118px;font-size:12px;line-height:20px}
.hours b{font-weight:600}
.foot-socials{position:absolute;left:834px;top:216px}
.foot-socials span{border-color:#ddd}
.to-top{position:absolute;left:1128px;top:180px;width:46px;height:46px;border-radius:50%;background:var(--olive)}
.copyright{position:absolute;left:0;top:3015px;width:1200px;height:43px;background:var(--olive-dark);color:var(--white);font-size:11.5px;text-align:center;line-height:43px}
</style>
</head>
<body>

<header class="site-header">
  <div class="brand">MQ OUTFITTERS</div>
  <nav class="main-nav">
    <a class="active" style="left:376px">Home</a>
    <a style="left:466px">About Us</a>
    <a style="left:553px">Products</a>
    <a style="left:640px">Resources</a>
    <a style="left:736px">Contact Us</a>
  </nav>
  <div class="socials header-socials"><span></span><span></span><span class="on"></span><span></span></div>
  <div class="quote-btn">Get A Quote</div>
</header>

<section class="hero" role="img" aria-label="Photo of a renovated kitchen with stainless fridge and marble counters">
  <div class="hero-title">When you want affordable</div>
  <div class="hero-sub">quality home construction services; think of us to do the job</div>
  <div class="hero-btn">Contact Us</div>
  <div class="dots"><span class="on"></span><span></span><span></span></div>
</section>

<div class="section-head" style="top:627px">
  <span class="ornament" role="img" aria-label="Small heading ornament"></span>
  <h2>ABOUT US</h2>
</div>
<div class="about-lead">Welcome to Brindle Cove Homes.</div>
<div class="about-text">
  When you want affordable, quality home construction services; think of us to do the job<br>
  <b>Since 1981</b> Warren Quill has built and remodeled over 400 homes and businesses. Let us be your contractor for the next project you start.<br>
  When quality, value and personal attention to detail are important
</div>
<div class="outline-btn">Click to more &nbsp;→</div>

<section class="products"></section>
<div class="section-head" style="top:995px">
  <span class="ornament" role="img" aria-label="Small heading ornament"></span>
  <h2>PRODUCTS</h2>
</div>

<div class="card-photo" style="left:208px;top:1092px;background:linear-gradient(135deg,#3a3632,#d9d5cc 60%,#b9b3a6)" role="img" aria-label="Photo of hands unrolling construction blueprints"></div>
<div class="card-cap" style="left:236px;top:1363px"><span class="num">01</span><span class="label">Pre Construction<br>Consultation</span></div>

<div class="card-photo" style="left:610px;top:1092px;background:linear-gradient(180deg,#c9c2a8,#b08a4e 70%,#8a6432)" role="img" aria-label="Photo of a new open-plan room with polished floor"></div>
<div class="card-cap" style="left:638px;top:1363px"><span class="num">02</span><span class="label">New Construction</span></div>

<div class="card-photo" style="left:208px;top:1466px;background:linear-gradient(160deg,#b8c6c2,#9aa9a5 50%,#8a6e52)" role="img" aria-label="Photo of a remodeled bathroom with soaking tub"></div>
<div class="card-cap" style="left:236px;top:1737px"><span class="num">03</span><span class="label">Remodeling / kitchens<br>and baths</span></div>

<div class="card-photo" style="left:610px;top:1466px;background:linear-gradient(180deg,#5b7a3a,#b8865a 50%,#c99a6e)" role="img" aria-label="Photo of a new wooden deck with railing"></div>
<div class="card-cap" style="left:638px;top:1737px"><span class="num">04</span><span class="label">Porches and Decks</span></div>

<div class="solid-btn">View All &nbsp;→</div>

<section class="resources" role="img" aria-label="Dim photo of builders at a construction site"></section>
<div class="section-head" style="top:2001px">
  <span class="ornament" role="img" aria-label="Small heading ornament"></span>
  <h2 style="color:#fff">RESOURCES</h2>
</div>
<div class="res-intro">Check out the following links for additional information and helpful resource.</div>

<div class="res-card" style="left:208px"><div style="width:74px;height:70px;background:linear-gradient(180deg,#f2c84b,#8fb7d6)" role="img" aria-label="Illustration of a building under construction with a crane"></div></div>
<div class="res-card" style="left:471px"><div class="res-name" style="color:#111">RIDGEWAY LUMBER</div></div>
<div class="res-card" style="left:734px"><div class="res-name" style="color:#bbb">FENWICK PLUMBING</div></div>

<div class="res-cap" style="left:208px">Take a look at this link to see a few of<br>the projects we have done recently</div>
<div class="res-cap" style="left:471px">Quality products and confident<br>service since 1944</div>
<div class="res-cap" style="left:734px">Great second generation<br>plumber</div>

<div class="map" role="img" aria-label="Street map showing the office location"></div>
<section class="consult">
  <h3>Book Free Consultation</h3>
  <div class="field" style="top:90px">Your Name</div>
  <div class="field" style="top:125px">Email</div>
  <div class="field" style="top:160px">Phone</div>
  <div class="field" style="top:195px;height:84px">Message ...</div>
  <div class="submit">SUBMIT</div>
</section>

<footer class="site-footer">
  <nav class="foot-nav"><span class="active">HOME</span><span>ABOUT US</span><span>PRODUCTS</span><span>RESOURCES</span><span>CONTACT US</span></nav>
  <div class="foot-rule"></div>
  <div class="contact">
    <div class="call"><b>Call.</b> 615-555-0142, 615-555-0187</div>
    <div><b>Email:</b> warren@brindlecoveroofing.com</div>
  </div>
  <div class="address"><b>Address:</b><br>Box 40512 Larkfield TN 37000</div>
  <div class="foot-brand">MQ OUTFITTERS</div>
  <div class="hours">
    <b>Business Hours:</b><br>
    Monday - Friday : &nbsp;7:00 am - 6:00 pm<br>
    Saturday: Closed<br>
    Sunday: Closed
  </div>
  <div class="socials foot-socials"><span></span><span></span><span style="border-color:var(--olive)"></span><span></span></div>
  <div class="to-top"><svg width="46" height="46" viewBox="0 0 46 46"><path d="M16 30 L23 15 L30 30" fill="none" stroke="#fff" stroke-width="2"/></svg></div>
</footer>
<div class="copyright">Copyright © 2021 MQ Outfitters. All Rights Reserved</div>

</body>
</html>
```